Flyer promoting Veltrane's workshops and credentials

We run Training workshops for the data analyst community. We'd like a flyer to sell our services using a style and colour scheme consistent with our website www.veltranepartners.co.uk . I've attached some background info and some existing e-brochures for different workshops to give a flavour for content (but these are poorly designed and we don't want a similar design!!). There's also an overview document which gives more direction. The flyer will be sent with an accompanying letter to Learning & Development decision makers as well as Anlaytical team managers. It's purpose would be to generate enquiries and bookings for primarliy our flagship workshop 'Turning Figures Into Real Gains'.

Target Market(s)

Learning and Development senior managers
Analytical team managers

Industry/Entity Type

Training

Other font styles liked:
• Similar to website for consistency

Requirements
Must have
• Good copy! Slick design more in line with European (UK) style advertising rather than US.
Nice to have
• Some humour,
Should not have
• should not be as boring and non-sales based as the website!! Website is not a great example!

```html
<!DOCTYPE html>
<html lang="en">
<head>
<meta charset="utf-8">
<title>Veltrane – Workshops for Data Analysts</title>
<link rel="stylesheet" href="https://fonts.googleapis.com/css2?family=Open+Sans:wght@400;600;700&family=Oswald:wght@600&family=PT+Sans+Narrow&family=Lora:ital@1&family=Arvo:ital,wght@1,700&display=swap">
<style>
:root{
  --navy:#0d2a66;
  --band:#1d3b6e;
  --orange:#e8871e;
  --ink:#1b1b1b;
  --paper:#ffffff;
}
*{margin:0;padding:0;box-sizing:border-box}
html,body{width:848px;height:1200px;overflow:hidden}
body{position:relative;background:linear-gradient(120deg,#0a1f55 0%,#1b5bb8 40%,#0c2a6e 70%,#061a4a 100%);font-family:"Open Sans",sans-serif;color:var(--ink)}
.sheet{position:absolute;left:32px;top:0;width:726px;height:1140px;background:var(--paper)}
.brand{position:absolute;left:42px;top:24px;font-family:"Open Sans",sans-serif;font-weight:700;font-size:40px;color:var(--band);letter-spacing:-1px;line-height:1}
.brand-dot{position:absolute;left:214px;top:26px;width:10px;height:10px;border-radius:50%;background:var(--orange)}
.tagline{position:absolute;left:48px;top:101px;font-family:"Lora",serif;font-style:italic;font-size:13px;color:var(--orange)}
.offer{position:absolute;left:236px;top:46px;width:612px;height:48px;background:var(--band);padding:8px 0 0 4px;white-space:nowrap}
.offer p{font-size:10.6px;color:var(--orange);letter-spacing:-0.1px}
.offer small{display:block;font-size:9.6px;color:#fff;padding-left:26px;margin-top:2px}
.rule{position:absolute;height:1px;background:var(--ink)}
.heading{position:absolute;font-family:"Arvo",serif;font-style:italic;font-weight:700;color:var(--orange);font-size:17px}
.row{position:absolute;left:80px;width:652px;height:112px;background:linear-gradient(180deg,#e6e6e6 0,#fff 22px)}
.row h3{position:absolute;left:72px;top:16px;width:170px;font-size:12.5px;font-weight:600;line-height:16px;text-transform:uppercase;color:#333;text-align:center}
.row .aud{position:absolute;left:72px;font-size:8.8px;line-height:13px;color:#222}
.row .aud b{display:block;font-size:10.5px;font-weight:700}
.row svg{position:absolute;left:254px;top:0}
.row .len{position:absolute;left:270px;top:12px;font-family:"Oswald",sans-serif;font-weight:600;font-size:29px;color:#fff}
.row .desc{position:absolute;left:445px;top:26px;width:174px;font-family:"PT Sans Narrow",sans-serif;font-size:10px;line-height:13.7px;text-align:justify;color:#111}
.intro,.quote{position:absolute;left:82px;width:672px;font-family:"Lora",serif;font-style:italic;color:var(--ink)}
.intro{top:754px;font-size:16px;line-height:20.5px}
.quote{font-size:14.2px;line-height:19px}
.quote cite{color:var(--orange);font-style:italic}
.footer{position:absolute;left:0;top:1140px;width:848px;height:60px;background:var(--band);text-align:center;color:#fff;padding-top:6px}
.footer .web{font-size:12.5px;font-weight:700}
.footer .addr{font-size:12px}
</style>
</head>
<body>
<div class="sheet"></div>
<div class="brand">Veltrane</div>
<div class="brand-dot"></div>
<div class="tagline">Workshops for Data Analysts</div>

<div class="offer">
  <p>Any bookings made with reference to this flyer will benefit from a 10% discount on fees until February 18th 2016</p>
  <small>(this may not be used in conjunction with any other promotional rates that may be available at the time of booking).</small>
</div>

<div class="heading" style="left:456px;top:130px">An overview of our Workshops</div>
<div class="rule" style="left:80px;top:152px;width:652px"></div>

<section class="row" style="top:162px">
  <h3 style="color:#9a9a9a">Turning Figures<br>Into Real Gains</h3>
  <div class="aud" style="top:52px"><b>Audience</b>Marketing Analysts | MI/BI Analysts<br>Risk Analysts | MI Analysts<br>Statistical Analysts | Financial Analysts</div>
  <svg width="176" height="94"><polygon points="0,0 176,0 176,30 0,92" fill="#9a9a9a"/></svg>
  <div class="len">2 Days</div>
  <p class="desc">A CPD accredited, interactive soft-skills workshop to improve the productivity and impact an analyst has on the organisation they support. Focusing on the three core themes of Communication, Presentation of Data and Planning.</p>
</section>

<section class="row" style="top:272px">
  <h3 style="color:var(--orange)">Delivering Analysis<br>for Impact</h3>
  <div class="aud" style="top:48px"><b>Audience</b>MI / BI Analysts | Risk Analysts<br>Insight/ Marketing Analysts<br>Statistical Analysts | Team managers</div>
  <svg width="176" height="94"><polygon points="0,0 176,0 176,30 0,92" fill="#f39a1e"/></svg>
  <div class="len">0.5 Days</div>
  <p class="desc">A half day seminar on the key behaviours and techniques information analysts/insight specialists need to employ in order to have a positive impact on their internal or external customers.</p>
</section>

<section class="row" style="top:382px">
  <h3 style="color:#b5b5b5;text-align:left">Influencing Skills</h3>
  <div class="aud" style="top:50px"><b>Audience</b>Marketing Analysts | MI/BI Analysts<br>Risk Analysts | Insight Analysts<br>Statistical Analysts | Financial Analysts</div>
  <svg width="176" height="94"><polygon points="0,0 176,0 176,30 0,92" fill="#cacaca"/></svg>
  <div class="len">1 Day</div>
  <p class="desc" style="top:28px">This workshop equips the analyst with a set of established techniques and principals to help them effectively influence their customers and internal decision makers - a key skill to ensuring personal and commercials goals are achieved.</p>
</section>

<section class="row" style="top:492px">
  <h3 style="color:#555;text-align:left;width:180px">&nbsp;&nbsp;&nbsp;Analytics in<br>Direct Marketing</h3>
  <div class="aud" style="top:62px"><b>Audience</b>Marketing Analysts | Direct Marketers</div>
  <svg width="176" height="94"><polygon points="0,0 176,0 176,30 0,92" fill="#707070"/></svg>
  <div class="len" style="top:20px">1 Day</div>
  <p class="desc" style="top:18px">A workshop to help delegates understand the tactical and strategic analytics which support the direct marketing life cycle. Includes practical exercises to reinforce the learnings. This worshop can only be hosted privately.</p>
</section>

<section class="row" style="top:602px">
  <h3 style="color:#333">Tailored Statistical<br>Workshops</h3>
  <div class="aud" style="top:56px"><b>Audience</b>Data Analysts | Statistical Analysts<br>Insight Analysts</div>
  <svg width="176" height="94"><polygon points="0,0 176,0 176,30 0,92" fill="#3a3a3a"/></svg>
  <div class="len" style="top:20px">1 Day</div>
  <p class="desc" style="top:24px">Customisable workshops - select the statistical methods and techniques you and your colleagues would like to cover and we'll provide you with a tailored day with practical examples and accompanying notes.</p>
</section>

<div class="heading" style="left:640px;top:726px">Testimonials</div>
<div class="rule" style="left:118px;top:748px;width:630px"></div>

<p class="intro">We aim for our workshops to be educational, interactive, practical and fun – we believe we deliver on this but don’t just take our word for it, here are some comments from our clients.</p>

<p class="quote" style="top:838px">“We took from the course a number of actionable learnings that we have put into practice and this has resulted in positive feedback and a happier more valued team. Recommend the course to new and experienced analysts alike.” - <cite>Tom Hadley, Brightwell Aid</cite></p>
<p class="quote" style="top:916px">"The workshop covered a lot of the areas I was concerned about in my role and how things were connected. I feel it has given me the confidence to alter some of my ways of working so I work more efficiently." - <cite>Maria Dunne, Kestrel Data Ltd</cite></p>
<p class="quote" style="top:995px;left:92px;width:662px">"I really enyoyed the session. It was pitched well for the skill set of attendees. I got a lot out of it in respect of tables/visuals formatting and have totally re-thought my intial views of providing/ producing data for my customers. Thankyou." - <cite>Janet Okoro, Northgate Systems</cite></p>
<p class="quote" style="top:1073px;left:96px;width:658px">"Kept me engaged throughout. Exercises were enjoyable and relevant. Easy to process/understand/ remember." - <cite>Owen Pike, Linkwave</cite></p>

<footer class="footer">
  <div class="web">www.veltranepartners.co.uk | info@veltranepartners.co.uk</div>
  <div class="addr">#4 Alder Yard, Hazelgrove, Stockport, Cheshire, SK9 4QT | Tel: 0161 555 0142 | Fax: 0845 555 0193</div>
</footer>
</body>
</html>
```